Postcard - We customize work clothing with your company name and/or logo

We customize work apparel for small to medium sized companies. We supply and customize most name brand tee shirts, polo shirts, dress shirts and hats with company name and logo. We also supply flame resistant shirts, coats, jeans, coveralls. We also make custom decals and stickers.We offer buying and ordering options catering to our customer’s needs. Explore the possibilities of custom apparel for uniforming, special events, team building and more. Give your organization an exceptional look with customized apparel designed for a lasting impact. Picture of Tee shirt with company name and logo goes here Picture of Polo shirt with company name and logo goes here Picture of Coveralls with name and logo Picture of a Base ball hat with company name and logo goes here. 10% off and no setup Fees with this promotional code – K-862

Target Market(s)

Small to medium sized companies

Industry/Entity Type

Clothing

Requirements
Must have
• The company name:
• Under The Lantern Stitched Garments and Such, LLC
• 20587 Tallowfern Road
• Cypress, Texas 77433
• Tel. (555) 947-6083
• email: underthelantern@mailvex.example
• Web page: www.stitchedgarmentsandsuch.example
• Web page: www.underthelantern.example

```html
<!DOCTYPE html>
<html lang="en">
<head>
<meta charset="utf-8">
<title>Under The Lantern – Postcard Back</title>
<link rel="stylesheet" href="https://fonts.googleapis.com/css2?family=Oswald:wght@500;600&family=Open+Sans:wght@400;700&family=Alegreya+Sans:wght@400;700&display=swap">
<style>
  :root {
    --stage: #3f3d3e;
    --paper: #ffffff;
    --sky: #1e9bd0;
    --sky-bright: #1ba7df;
    --alert-red: #d1232a;
    --ribbon-yellow: #fff200;
    --ribbon-ink: #1d6fb8;
    --navy: #1f3a8e;
    --ink: #2b2b2b;
    --rule: #8a8a8a;
  }
  * { margin: 0; padding: 0; box-sizing: border-box; }
  html, body { width: 1200px; height: 930px; overflow: hidden; }
  body { background: var(--stage); position: relative; font-family: "Open Sans", Arial, sans-serif; }

  .postcard {
    position: absolute; left: 66px; top: 84px;
    width: 1068px; height: 761px;
    background: var(--paper);
    overflow: hidden;
  }
  .about-band {
    position: absolute; left: 0; top: 0; width: 858px; height: 201px;
    background: var(--sky);
  }
  .about-band .perforation {
    position: absolute; left: 0; top: 186px; width: 858px; height: 0;
    border-top: 2px dashed var(--paper);
  }
  .ribbon { position: absolute; display: block; }
  .ribbon text { font-family: "Oswald", "Arial Narrow", sans-serif; font-weight: 500; }

  .about-label { left: 55px; top: 23px; }
  .about-copy {
    position: absolute; left: 56px; top: 63px; width: 590px;
    color: var(--paper); font-size: 15px; line-height: 21px;
  }
  .about-copy strong { font-weight: 700; }

  .stamp-box {
    position: absolute; left: 905px; top: 29px; width: 126px; height: 145px;
    border: 1px solid var(--rule);
  }
  .tag-badge { position: absolute; left: 627px; top: 43px; }
  .tag-badge text {
    font-family: "Oswald", "Arial Narrow", sans-serif; font-weight: 500;
    font-size: 30px; fill: var(--paper);
  }

  .intro {
    position: absolute; left: 62px; top: 220px; width: 560px;
    color: var(--ink); font-size: 16px; line-height: 21px;
  }
  .offer-label { left: 60px; top: 303px; }
  .tagline {
    position: absolute; left: 194px; top: 303px;
    font-family: "Alegreya Sans", Arial, sans-serif; font-weight: 700;
    font-size: 25px; color: var(--navy);
  }
  .service-list {
    position: absolute; list-style: none;
    font-family: "Alegreya Sans", Arial, sans-serif;
    font-size: 20px; line-height: 26.3px; color: var(--ink);
  }
  .service-list li::before {
    content: "•"; color: var(--sky-bright); margin-right: 6px;
  }
  .service-list.primary { left: 59px; top: 342px; }
  .service-list.secondary { left: 249px; top: 340px; }
  .order-label { left: 257px; top: 543px; }

  .contact {
    position: absolute; left: 61px; top: 593px;
    font-family: "Alegreya Sans", Arial, sans-serif; font-weight: 700;
  }
  .contact .phone { color: var(--sky-bright); font-size: 31px; line-height: 36px; }
  .contact .web { color: var(--alert-red); font-size: 22px; line-height: 26px; }

  .address-line {
    position: absolute; left: 720px; width: 287px; height: 0;
    border-top: 1px solid var(--rule);
  }
</style>
</head>
<body>
  <main class="postcard">
    <section class="about-band">
      <svg class="ribbon about-label" width="90" height="30" viewBox="0 0 90 30" aria-hidden="false">
        <polygon points="0,0 90,0 80,15 90,30 0,30" fill="var(--ribbon-yellow)"/>
        <polyline points="3,3 83,3 74,15 83,27 3,27" fill="none" stroke="var(--ribbon-ink)" stroke-width="1" stroke-dasharray="3 2"/>
        <text x="8" y="22" font-size="17" fill="var(--ribbon-ink)">ABOUT US</text>
      </svg>
      <p class="about-copy"><strong>Under The Lantern Stitched Garments and Such, LLC (UTL)</strong> is a family owned business. We stared at the Tallowfern Rd location in August of 2015. The company was successfully formed as a Limited Liability Corporation (LLC) in April 2015. UTL is unique in that we have equipment at our Tallowfern Rd location that customizes apparel. We have all types of machines .</p>
      <div class="perforation"></div>
    </section>

    <div class="stamp-box"></div>

    <svg class="tag-badge" width="220" height="220" viewBox="0 0 220 220">
      <circle cx="110" cy="110" r="110" fill="var(--paper)"/>
      <circle cx="110" cy="110" r="102" fill="var(--alert-red)"/>
      <circle cx="110" cy="110" r="93" fill="none" stroke="var(--paper)" stroke-width="1.2" stroke-dasharray="4 3"/>
      <circle cx="110" cy="36" r="8" fill="var(--paper)"/>
      <text x="110" y="83" text-anchor="middle">EMERGENCIES</text>
      <text x="110" y="115" text-anchor="middle">AND SMALL</text>
      <text x="110" y="148" text-anchor="middle">ORDERS</text>
      <text x="110" y="180" text-anchor="middle">WELCOME</text>
    </svg>

    <p class="intro">We supply and customize most name brand T-Shirts, polo shirts, dress shirts and hats with company name and logo. We also supply flame resistant shirts, coats, jeans, coveralls.</p>

    <svg class="ribbon offer-label" width="88" height="30" viewBox="0 0 88 30">
      <polygon points="0,0 88,0 78,15 88,30 0,30" fill="var(--alert-red)"/>
      <polyline points="3,3 81,3 72,15 81,27 3,27" fill="none" stroke="var(--paper)" stroke-width="1" stroke-dasharray="3 2"/>
      <text x="7" y="22" font-size="17" fill="var(--paper)">WE OFFER</text>
    </svg>
    <h2 class="tagline">We make good Stuff Better</h2>

    <ul class="service-list primary">
      <li>Embroidery</li>
      <li>Dig Printing</li>
      <li>Rhinestones</li>
      <li>Spangles</li>
      <li>Sublamination</li>
      <li>Vinyl Lettering</li>
      <li>Decals</li>
      <li>Fund Raisers</li>
      <li>Special Event</li>
    </ul>
    <ul class="service-list secondary">
      <li>Bridal Showers</li>
      <li>Family Reunions</li>
      <li>Promotional Products</li>
      <li>Monograming</li>
      <li>Window Lettering</li>
      <li>Graphics And Stickers</li>
      <li>Team And Business Logos</li>
    </ul>

    <svg class="ribbon order-label" width="222" height="32" viewBox="0 0 222 32">
      <polygon points="0,0 222,0 212,16 222,32 0,32 10,16" fill="var(--alert-red)"/>
      <polyline points="13,3 215,3 206,16 215,29 13,29" fill="none" stroke="var(--paper)" stroke-width="1" stroke-dasharray="3 2"/>
      <text x="111" y="23" text-anchor="middle" font-size="18" fill="var(--paper)">PLACE YOUR ORDER NOW !</text>
    </svg>

    <div class="contact">
      <p class="phone">Call : (555) 947-6083</p>
      <p class="web">www.underthelantern.example</p>
    </div>

    <div class="address-line" style="top:384px"></div>
    <div class="address-line" style="top:459px"></div>
    <div class="address-line" style="top:534px"></div>
  </main>
</body>
</html>
```